Post Lockdown Ortho Special

We are running a special for (Ortho) Braces/Clear Aligner (Quorventa), till July 31st 2020. Up to $2,000 off with free Consultation and Xrays.

We need a ad to run in different formats.

Maybe something with: what better time to get braces when you have to wear a mask all the time.

Trying to rebuild our business and get people in for free consultations.

```html
<!DOCTYPE html>
<html lang="en">
<head>
<meta charset="utf-8">
<title>Ridgeline Family Dentistry – Post Lockdown Ortho Special</title>
<link rel="stylesheet" href="https://fonts.googleapis.com/css2?family=Montserrat:wght@400;500;600;700;800&display=swap">
<style>
  :root {
    --backdrop: #5f5f61;
    --paper: #ffffff;
    --purple: #65449a;
    --purple-text: #5a3c91;
    --lilac: #b398c6;
    --lilac-soft: #d9c6e4;
    --photo-skin: #e6c3b0;
    --photo-mask: #c9b3a6;
    --photo-light: #f4e7e2;
  }
  * { margin: 0; padding: 0; box-sizing: border-box; }
  html, body {
    width: 1098px; height: 1200px; overflow: hidden;
    background: var(--backdrop);
    font-family: "Montserrat", sans-serif;
  }
  .flyer {
    position: absolute; left: 180px; top: 30px;
    width: 738px; height: 1140px;
    background: var(--paper);
    display: flex; flex-direction: column;
  }
  .brand {
    height: 199px;
    display: flex; align-items: center; justify-content: center; gap: 22px;
  }
  .brand__dot {
    width: 96px; height: 96px; border-radius: 50%;
    background: var(--lilac);
  }
  .brand__text { color: var(--purple-text); font-weight: 600; }
  .brand__name { font-size: 38px; letter-spacing: 1px; line-height: 1; }
  .brand__tag {
    font-size: 12px; letter-spacing: 6.5px; text-transform: uppercase;
    margin-top: 6px; padding-bottom: 6px; border-bottom: 1px solid var(--lilac);
  }
  .brand__doctor {
    font-size: 12px; letter-spacing: 1.5px; text-transform: uppercase;
    margin-top: 6px; text-align: center; color: #7b6a8e;
  }
  .headline-band {
    height: 90px; background: var(--purple); color: #fff;
    display: flex; align-items: center; justify-content: center;
    font-size: 32px; font-weight: 400; letter-spacing: -0.3px;
  }
  .headline-band strong { font-weight: 800; margin-left: 10px; }
  .gap-top { height: 9px; }
  .photos { height: 303px; display: block; }
  .gap-bottom { height: 8px; }
  .message-band {
    height: 185px; background: var(--purple); color: #fff;
    display: flex; align-items: center; justify-content: center;
    text-align: center; font-weight: 700; font-size: 22px;
    letter-spacing: 2.6px; line-height: 1.36; text-transform: uppercase;
  }
  .offer {
    height: 251px; color: var(--purple-text);
    display: flex; flex-direction: column; align-items: center; justify-content: center;
    text-align: center;
  }
  .offer__amount { font-size: 60px; font-weight: 500; letter-spacing: -0.5px; line-height: 1; }
  .offer__amount strong { font-weight: 800; }
  .offer__details { font-size: 25px; font-weight: 500; line-height: 1.25; margin-top: 16px; }
  .offer__deadline {
    margin-top: 18px; font-size: 20px; font-weight: 500;
    border: 1.5px solid var(--lilac); border-radius: 20px; padding: 6px 16px;
  }
  .call-band {
    height: 95px; background: var(--lilac); color: #fff;
    display: flex; align-items: center; justify-content: center; gap: 12px;
    font-size: 40px;
  }
  .call-band__label { font-weight: 400; }
  .call-band__number { font-weight: 800; letter-spacing: -0.5px; }
  .call-band svg { width: 44px; height: 44px; }
</style>
</head>
<body>
  <main class="flyer">
    <header class="brand">
      <div class="brand__dot"></div>
      <div class="brand__text">
        <div class="brand__name">RIDGELINE</div>
        <div class="brand__tag">Family Dentistry</div>
        <div class="brand__doctor">Dr Maren Holloway</div>
      </div>
    </header>

    <section class="headline-band">POST LOCKDOWN <strong>ORTHO SPECIAL</strong></section>
    <div class="gap-top"></div>

    <svg class="photos" viewBox="0 0 738 303" preserveAspectRatio="none">
      <defs>
        <linearGradient id="maskedGrad" x1="0" y1="0" x2="0" y2="1">
          <stop offset="0" stop-color="var(--photo-skin)"/>
          <stop offset="1" stop-color="var(--photo-mask)"/>
        </linearGradient>
        <linearGradient id="smileGrad" x1="0" y1="0" x2="1" y2="0">
          <stop offset="0" stop-color="var(--photo-skin)"/>
          <stop offset="1" stop-color="var(--photo-light)"/>
        </linearGradient>
      </defs>
      <polygon role="img" aria-label="Photo of a woman wearing a surgical face mask" points="0,0 220,0 370,303 0,303" fill="url(#maskedGrad)"/>
      <polygon role="img" aria-label="Close-up photo of a smiling mouth with dental braces" points="227,0 727,0 727,303 379,303" fill="url(#smileGrad)"/>
    </svg>

    <div class="gap-bottom"></div>
    <section class="message-band">
      <p>What better time to get braces<br>when you have to wear<br>a mask all the time</p>
    </section>

    <section class="offer">
      <p class="offer__amount">UP TO <strong>$2,000 OFF</strong></p>
      <p class="offer__details">ON BRACES/CLEAR ALIGNER (QUORVENTA)<br>WITH FREE CONSULTATION AND XRAYS</p>
      <p class="offer__deadline">OFFER TILL JULY 31ST 2020</p>
    </section>

    <footer class="call-band">
      <span class="call-band__label">CALL TODAY</span>
      <svg viewBox="0 0 44 44" aria-hidden="true">
        <circle cx="22" cy="22" r="20" fill="none" stroke="#fff" stroke-width="2.5"/>
        <path d="M15 12c1.5-1 2.6-.6 3.3.6l2 3.4c.6 1 .3 2-.6 2.7l-1.3 1c1 2.6 3 4.6 5.6 5.7l1-1.3c.7-.9 1.8-1.2 2.8-.6l3.3 2c1.2.7 1.5 1.9.5 3.3-1.4 2-3.4 2.6-5.6 1.8-5.5-2-9.7-6.2-11.6-11.7-.8-2.3-.2-4.4 1.6-6.2z" fill="none" stroke="#fff" stroke-width="2"/>
        <path d="M25 13a7 7 0 0 1 6 6M25 9a11 11 0 0 1 10 10" fill="none" stroke="#fff" stroke-width="2" stroke-linecap="round"/>
      </svg>
      <span class="call-band__number">928 555 0147</span>
    </footer>
  </main>
</body>
</html>
```